" A maioria das empresas tem dificuldades em lidar com o quadro de funcionários. A consultoria entra fornecendo todo o suporte com treinamentos para melhoria do clima e das relações interpessoais, melhoria do atendimento ao cliente, desenvolve líderes e os capacita para lidar de maneira mais adequada com os conflitos da equipe. Além disso, também realizamos todo o processo de recrutamento e seleção. Entre outros serviços. "

```html
<!DOCTYPE html>
<html lang="pt-BR">
<head>
<meta charset="utf-8">
<title>Verta — Orçamento</title>
<link rel="stylesheet" href="https://fonts.googleapis.com/css2?family=Montserrat:wght@400;500;600;700&display=swap">
<style>
  :root {
    --backdrop: #06093a;
    --paper: #ffffff;
    --paper-shade: #e2e3e6;
    --ink: #2c2c2c;
    --rule: #6b6b6b;
    --accent: #f0a323;
    --mark-tone: #eeeef0;
  }
  * { box-sizing: border-box; margin: 0; padding: 0; }
  html, body {
    width: 1200px; height: 1200px; overflow: hidden;
    background: var(--backdrop);
    font-family: "Montserrat", sans-serif;
    color: var(--ink);
  }
  .letterhead {
    position: absolute; left: 223px; top: 41px;
    width: 785px; height: 1111px;
    background: linear-gradient(100deg, var(--paper) 0%, var(--paper) 32%, var(--paper-shade) 100%);
    overflow: hidden;
  }
  .brand { position: absolute; left: 36px; top: 42px; }
  .brand-name {
    display: flex; align-items: center; gap: 8px;
    font-size: 38px; font-weight: 600; letter-spacing: 1px; line-height: 1;
    color: var(--ink);
  }
  .brand-square { width: 20px; height: 36px; background: var(--accent); }
  .brand-tagline {
    margin-top: 5px; margin-left: 28px;
    font-size: 12px; color: var(--accent); letter-spacing: .5px;
  }
  .form-title, .section-title {
    position: absolute; left: 0; width: 785px; text-align: center;
    font-size: 19px; font-weight: 500; line-height: 1;
  }
  .form-title { top: 190px; }
  .section-title { top: 440px; }
  .field-label {
    position: absolute; font-size: 17px; line-height: 1;
  }
  .field-line {
    position: absolute; height: 0; border-bottom: 1.5px solid var(--rule);
  }
  .brand-watermark {
    position: absolute; left: 0; top: 428px; width: 400px; bottom: 0;
    background: linear-gradient(180deg, rgba(238,238,240,0) 0%, var(--mark-tone) 18%, #ebebee 70%, rgba(238,238,240,.4) 100%);
  }
  .contact-bar {
    position: absolute; top: 1048px; left: 172px;
    display: flex; align-items: center; gap: 22px;
    font-size: 11px; line-height: 1.2;
  }
  .contact-item { display: flex; align-items: center; gap: 6px; }
  .contact-icon { width: 20px; height: 20px; }
  .accent-band {
    position: absolute; left: 168px; bottom: 0; width: 478px; height: 9px;
    background: var(--accent); border-radius: 6px 6px 0 0;
  }
</style>
</head>
<body>
<main class="letterhead">
  <div class="brand-watermark" role="img" aria-label="Faint large brand decoration"></div>

  <header class="brand">
    <div class="brand-name"><span class="brand-square"></span>VERTA</div>
    <div class="brand-tagline">Consultoria em RH</div>
  </header>

  <h1 class="form-title">Orçamento</h1>

  <span class="field-label" style="left:36px; top:254px;">Nome Cliente</span>
  <span class="field-line" style="left:192px; width:341px; top:271px;"></span>
  <span class="field-label" style="left:540px; top:254px;">Data</span>
  <span class="field-line" style="left:593px; width:156px; top:271px;"></span>

  <span class="field-label" style="left:36px; top:312px;">Serviço</span>
  <span class="field-line" style="left:118px; width:631px; top:329px;"></span>

  <span class="field-label" style="left:36px; top:362px;">Valor</span>
  <span class="field-line" style="left:118px; width:631px; top:379px;"></span>

  <h2 class="section-title">Objetivo</h2>

  <footer class="contact-bar">
    <div class="contact-item">
      <svg class="contact-icon" viewBox="0 0 20 20"><circle cx="10" cy="10" r="9" fill="none" stroke="#2c2c2c" stroke-width="1.3"/><path d="M7 5.5l2 2-1 1.5c.6 1.4 1.6 2.4 3 3l1.5-1 2 2-1.3 1.5C9.5 14.5 5.5 10.5 5.5 6.8z" fill="#2c2c2c"/></svg>
      <span>(00) 0000-0000</span>
    </div>
    <div class="contact-item">
      <svg class="contact-icon" viewBox="0 0 20 20"><circle cx="10" cy="10" r="9" fill="none" stroke="#2c2c2c" stroke-width="1.3"/><path d="M10 4.5a3.5 3.5 0 0 1 3.5 3.5c0 2.6-3.5 7-3.5 7s-3.5-4.4-3.5-7A3.5 3.5 0 0 1 10 4.5z" fill="#2c2c2c"/><circle cx="10" cy="8" r="1.3" fill="#fff"/></svg>
      <span>R. Seu Endereço<br>nº 2020 - Cidade - ES</span>
    </div>
    <div class="contact-item">
      <svg class="contact-icon" viewBox="0 0 20 20"><circle cx="10" cy="10" r="9" fill="none" stroke="#2c2c2c" stroke-width="1.3"/><rect x="5" y="6.5" width="10" height="7" fill="none" stroke="#2c2c2c" stroke-width="1.2"/><path d="M5 6.5l5 4 5-4" fill="none" stroke="#2c2c2c" stroke-width="1.2"/></svg>
      <span>contato@vertarh.com</span>
    </div>
  </footer>

  <div class="accent-band"></div>
</main>
</body>
</html>
```